Design a box for EV Charging Cables - Electric Cars

https://files.plomtrex.example/doc/7qRwLm2ZxNa9/view

We are looking to design a box to package our EV charging cables. This box needs to be 40cm x 40cm x 11cm.

It needs to include:
- Our logo
- Images of our products
- Accreditations

My websites are:
https://voltharbor.co.uk/
https://www.plugmerrow.co.uk/
https://www.zandrel-amp.co.uk/

Logo:
https://pixdrop.example/Kq8Tz2L
https://pixdrop.example/Rw4Hn9B
https://pixdrop.example/Jd7Pv3X
https://pixdrop.example/Ny6Qb5G

Rather than having a list of products. I would like to have tick boxes:
1st tick box: Connector Type From: (Type 2, 3 Pin),
2nd tick box: Connector Type To: (Type 1, Type 2),
3rd tick box: Amp/Charge Speed (13amp/16amp/32amp/32amp - 3 Phase)
4th tick box: Length (5m/10m/15m)

Target Market(s)

People who own electric cars

Industry/Entity Type

Automotive

Colors

Designer to choose colors to be used in the design.

Requirements
Must have
• Our colours, logo, list of products we sell
Nice to have
• Rather than having a list of products. I would like to have tick boxes: 1st tick box should be: Connector Type From: (Type 2, 3 Pin), Connector Type To: (Type 1, Type 2), Third: Amp/Charge Speed (13amp/16amp/32amp/32amp - 3 Phase) Third: Length (5m/10m/15m)
Should not have
• Transparent Section

```html
<!DOCTYPE html>
<html lang="en">
<head>
<meta charset="utf-8">
<title>Zandrel Amp – EV Charging Cables Box</title>
<link rel="stylesheet" href="https://fonts.googleapis.com/css2?family=Barlow+Condensed:wght@600;700&family=Barlow:wght@500;700&display=swap">
<style>
  :root{
    --bg:#a8c8d8;
    --panel-white:#f4f4f4;
    --panel-edge:#e6e6e6;
    --green:#5f9f1f;
    --green-side:#6aab27;
    --lime:#a3c33c;
    --grey-band:#d4d4d4;
    --ink:#1b1b1b;
    --white:#ffffff;
  }
  *{box-sizing:border-box;margin:0;padding:0}
  html,body{width:1200px;height:1200px;overflow:hidden;background:var(--bg)}
  body{font-family:"Barlow",sans-serif;position:relative}

  .dieline{position:absolute;left:88px;top:179px;width:1024px;height:842px}
  .panel{position:absolute}

  /* top lid */
  .panel-top{left:182px;top:0;width:660px;height:182px;background:var(--panel-white);
    border-bottom:1px solid var(--panel-edge);display:flex;align-items:center;justify-content:center}

  /* left side: product options */
  .panel-left{left:0;top:182px;width:182px;height:660px;
    background:linear-gradient(180deg,#74b52f 0%,var(--green-side) 100%);
    color:var(--white);padding:38px 18px 30px}
  .option-group{border:1.5px solid rgba(255,255,255,.85);padding:8px 9px 9px;margin-bottom:10px}
  .option-title{font-size:12px;font-weight:700;margin-bottom:6px;letter-spacing:.2px}
  .option-list{display:grid;grid-template-columns:1fr 1fr;gap:5px 6px;list-style:none}
  .option-list.single{grid-template-columns:1fr}
  .option{display:flex;align-items:center;gap:5px;font-size:11px}
  .tick-box{width:10px;height:10px;border:1.3px solid var(--white);flex:none}
  .websites{margin-top:26px;font-size:11px;line-height:1.7;list-style:none;text-align:right}

  /* shared brand mark */
  .brand-mark{display:flex;align-items:center;gap:8px;font-family:"Barlow Condensed",sans-serif;
    font-weight:700;color:var(--green);letter-spacing:1px;white-space:nowrap}
  .brand-mark .dot{width:14px;height:14px;border-radius:50%;background:var(--green);flex:none}
  .panel-top .brand-mark{font-size:34px}

  /* front face */
  .panel-front{left:182px;top:182px;width:660px;height:660px;
    background:linear-gradient(180deg,#f7f7f7 0%,#efefef 65%,#e2e2e2 100%);overflow:hidden}
  .panel-front .brand-mark{position:absolute;left:58px;top:150px;font-size:40px}
  .retailer{position:absolute;right:30px;top:98px;display:flex;align-items:center;gap:7px;
    font-weight:700;font-size:15px;color:var(--ink);border-bottom:2px solid var(--green);padding-bottom:2px}
  .retailer .dot{width:11px;height:11px;border-radius:50%;background:var(--ink)}
  .headline{position:absolute;left:58px;top:290px}
  .tagline{display:inline-block;background:var(--lime);color:var(--white);
    font-family:"Barlow Condensed",sans-serif;font-weight:600;font-size:29px;
    padding:2px 10px;letter-spacing:.5px}
  .title{font-family:"Barlow Condensed",sans-serif;font-weight:700;color:var(--green);
    font-size:86px;line-height:.94;margin-top:8px;letter-spacing:-.5px}
  .product-photo{position:absolute;right:30px;top:130px;width:260px;height:530px;
    background:linear-gradient(160deg,#2a2a2a 0%,#161616 45%,#3b7e1c 55%,#161616 70%,#111 100%);
    border-radius:40px 40px 0 0}

  /* right side */
  .panel-right{left:842px;top:182px;width:182px;height:660px;background:var(--panel-white);
    border-left:1px solid var(--panel-edge)}
  .side-band{position:absolute;left:22px;top:38px;width:64px;height:430px;background:var(--lime);
    display:flex;align-items:center;justify-content:center}
  .side-band .band-text{transform:rotate(-90deg);white-space:nowrap;
    font-family:"Barlow Condensed",sans-serif;font-weight:600;color:var(--white);font-size:22px;line-height:1}
  .side-title{position:absolute;left:92px;top:38px;width:60px;height:430px;display:flex;align-items:center;justify-content:center}
  .side-title span{transform:rotate(-90deg);white-space:nowrap;font-family:"Barlow Condensed",sans-serif;
    font-weight:700;color:var(--green);font-size:46px;line-height:1}
  .side-brand{position:absolute;left:22px;top:488px;width:130px;height:160px;
    display:flex;align-items:center;justify-content:center}
  .side-brand .brand-mark{transform:rotate(-90deg);font-size:26px;gap:6px}
  .side-brand .brand-mark .dot{width:11px;height:11px}
</style>
</head>
<body>
<main class="dieline">
  <section class="panel panel-top">
    <div class="brand-mark"><span class="dot"></span>Zandrel Amp</div>
  </section>

  <aside class="panel panel-left">
    <div class="option-group">
      <p class="option-title">Connector Type From</p>
      <ul class="option-list">
        <li class="option"><span class="tick-box"></span>Type 2</li>
        <li class="option"><span class="tick-box"></span>3 Pin</li>
      </ul>
    </div>
    <div class="option-group">
      <p class="option-title">Connector Type To</p>
      <ul class="option-list">
        <li class="option"><span class="tick-box"></span>Type 1</li>
        <li class="option"><span class="tick-box"></span>Type 2</li>
      </ul>
    </div>
    <div class="option-group">
      <p class="option-title">Amp/Charge Speed</p>
      <ul class="option-list">
        <li class="option"><span class="tick-box"></span>13amp</li>
        <li class="option"><span class="tick-box"></span>16amp</li>
      </ul>
      <ul class="option-list single" style="margin-top:5px">
        <li class="option"><span class="tick-box"></span>32amp (3 phase)</li>
        <li class="option"><span class="tick-box"></span>32amp</li>
      </ul>
    </div>
    <div class="option-group">
      <p class="option-title">Length</p>
      <ul class="option-list">
        <li class="option"><span class="tick-box"></span>5m</li>
        <li class="option"><span class="tick-box"></span>10m</li>
        <li class="option"><span class="tick-box"></span>15m</li>
      </ul>
    </div>
    <ul class="websites">
      <li>www.voltharbor.co.uk</li>
      <li>www.plugmerrow.co.uk</li>
      <li>www.zandrel-amp.co.uk</li>
    </ul>
  </aside>

  <section class="panel panel-front">
    <div class="retailer"><span class="dot"></span>Plugmerrow</div>
    <div class="brand-mark"><span class="dot"></span>Zandrel Amp</div>
    <div class="headline">
      <span class="tagline">ELECTRIC VEHICLE</span>
      <h1 class="title">CHARGING<br>CABLES</h1>
    </div>
    <div class="product-photo" role="img" aria-label="Product photo: black and green Type 2 charging connector with dust cap, cable and UK three-pin plug"></div>
  </section>

  <aside class="panel panel-right">
    <div class="side-band"><span class="band-text">ELECTRIC VEHICLE</span></div>
    <div class="side-title"><span>CHARGING CABLES</span></div>
    <div class="side-brand">
      <div class="brand-mark"><span class="dot"></span>Zandrel Amp</div>
    </div>
  </aside>
</main>
</body>
</html>
```